Website for Tech Venture Capital - Korvend Capital

We need a website for Korvend Capital.
Slogan:
Helping Ambitious Entrepreneurs Start and Build Great Companies.

Korvend Capital is a venture capital looking to support and invest in young talent within the technology and digital marketing industry. We wish for a website that reflects that while matching our logo and color palette.

Our Domain is: https://korvend.vc/
We would like to have these considered as references/inspiration for our website:
https://www.tilmorefund.com/
https://www.brunhalecap.com/israel/

You can find the desired structure and the zip file attached.
There is a color palette attached as well.
Social media pages to be used:
https://www.linkedin.com/in/jonmirtaveski/
https://www.linkedin.com/in/tomas-dune-rok/
https://www.linkedin.com/in/corvish/

Target Market(s)

Young Tech and Digital Marketing Entrepreneurs

Industry/Entity Type

Tech, Finance

Coding

Coded - Design and coding required

Number of Pages Required

4 page

Font styles to use
Sans Serif

Colors
0054AA
0677BA
7BADD7
CADEEF
E8F1F8
0094D4
00A9DD
6FCCEA
C7EBF8
E9F6FB

Requirements
Must have
• Please see attached files. WordPress sites strongly preferred.

```html
<!DOCTYPE html>
<html lang="en">
<head>
<meta charset="utf-8">
<title>Korvend Capital – Website Design</title>
<link href="https://fonts.googleapis.com/css2?family=Lato:wght@400;700&family=Playfair+Display:wght@400;500&display=swap" rel="stylesheet">
<style>
:root{
  --navy:#0d193f;
  --blue:#1ca3de;
  --white:#ffffff;
  --offwhite:#f7f7f7;
  --board:#d1d4dc;
  --muted:#8a8f9c;
  --ink:#2b2f3a;
  --line:#e6e7ea;
  --serif:'Playfair Display', Georgia, serif;
  --sans:'Lato', Arial, sans-serif;
}
*{margin:0;padding:0;box-sizing:border-box}
html,body{width:1200px;height:2782px;overflow:hidden}
body{background:var(--board);font-family:var(--sans);color:var(--ink);position:relative}
.abs{position:absolute}

/* board header */
.brand-mark{left:254px;top:140px;font:700 34px/1 var(--sans);color:var(--navy);display:flex;align-items:center;gap:10px}
.brand-mark .dot{width:14px;height:14px;background:var(--navy)}
.divider-v{width:1px;height:82px;top:121px;background:#9aa0ad}
.spec-title{font:400 24px/1 var(--serif);color:var(--navy)}
.spec-item{font:400 17px/1 var(--serif);color:#5b6070}
.spec-item.sans{font:400 15px/1 var(--sans)}
.swatch{width:38px;height:38px;border-radius:50%;top:152px}
.swatch-code{top:196px;font:400 9px/1 var(--sans);color:#5b6070;width:50px;text-align:center}

/* generic hero screen */
.screen{position:absolute;overflow:hidden;background:var(--navy);box-shadow:0 10px 30px rgba(13,25,63,.25)}
.screen .s-top{background:var(--navy);display:flex;align-items:center;justify-content:space-between;color:#fff}
.screen .s-nav{background:#fff;display:flex;align-items:center;justify-content:space-between}
.screen .s-logo{font-weight:700;color:var(--navy)}
.screen .s-links{display:flex;color:var(--ink)}
.screen .s-links .on{color:var(--blue)}
.screen .s-hero{position:absolute;left:0;right:0;bottom:0;background:linear-gradient(135deg,#4d6584 0%,#2d405d 45%,#6b819e 100%)}
.screen .s-hero::after{content:"";position:absolute;inset:0;background:linear-gradient(90deg,rgba(13,25,63,.55),rgba(13,25,63,.15))}
.screen .s-copy{position:absolute;z-index:1;color:#fff}
.screen .s-label{letter-spacing:.15em;text-transform:uppercase}
.screen h2{font-family:var(--serif);font-weight:400}
.screen .s-btn{background:var(--blue);color:#fff;font-weight:700;display:inline-flex;align-items:center;justify-content:center}
.li-sq{display:inline-block;background:#3a4566}
.li-sq.blue{background:#0a66c2}

/* desktop page */
.page{position:absolute;background:#fff;overflow:hidden}
.d-page{left:155px;top:859px;width:731px;height:1805px}
.topbar{background:var(--navy);color:#fff;display:flex;align-items:center;justify-content:space-between}
.navbar{background:#fff;display:flex;align-items:center;justify-content:space-between;border-bottom:1px solid var(--line)}
.logo-text{font-weight:700;color:var(--navy)}
.nav-links{display:flex;list-style:none}
.nav-links .active{color:var(--blue);border-bottom:1px solid var(--blue)}
.hero{position:relative;background:linear-gradient(135deg,#55708f 0%,#2e4462 40%,#3c5676 70%,#8096b0 100%)}
.hero::after{content:"";position:absolute;inset:0;background:linear-gradient(90deg,rgba(13,25,63,.55),rgba(13,25,63,.1))}
.hero-copy{position:absolute;z-index:1;color:#fff}
.eyebrow{text-transform:uppercase;letter-spacing:.2em}
.btn{background:var(--blue);color:#fff;font-weight:700;display:flex;align-items:center;justify-content:center;letter-spacing:.03em}
.about{background:var(--navy);color:#fff;position:relative}
.about .eyebrow{color:var(--blue)}
.serif-title{font-family:var(--serif);font-weight:400}
.about p a{color:#fff}
.collage{background:linear-gradient(160deg,#c7cedb 0%,#7e8aa5 45%,#2f3d63 100%);opacity:.85}
.team{position:relative;background:#fff}
.member{position:absolute;background:var(--offwhite);border:1px solid #eeeeef;text-align:center}
.portrait{background:linear-gradient(180deg,#f1f1f1 0%,#d9d9dc 100%)}
.member .name{font-family:var(--serif);color:var(--navy)}
.member .role{color:var(--muted)}
.contact{position:relative;background:#fff}
.contact .eyebrow{color:#555}
.office-name{font-family:var(--serif);color:var(--navy)}
.office-addr{color:#6a6f7b}
.footer{background:var(--navy);color:#fff;position:relative}
.footer .f-head{font-family:var(--serif);font-weight:400}
.footer ul{list-style:none}
.footer a,.contact a{color:inherit}

/* labels */
.side-label{font:400 20px/1 var(--sans);letter-spacing:.45em;color:var(--navy);transform:rotate(-90deg);transform-origin:left top;white-space:nowrap}
</style>
</head>
<body>

<!-- Board header -->
<div class="abs brand-mark"><span class="dot"></span>Korvend Capital</div>
<div class="abs divider-v" style="left:513px"></div>
<div class="abs spec-title" style="left:573px;top:120px">Fonts:</div>
<div class="abs spec-item" style="left:573px;top:163px">Playfair Display</div>
<div class="abs spec-item sans" style="left:573px;top:188px">Lato</div>
<div class="abs divider-v" style="left:759px"></div>
<div class="abs spec-title" style="left:818px;top:120px">Colors:</div>
<div class="abs swatch" style="left:819px;background:#0d193f"></div>
<div class="abs swatch" style="left:866px;background:#1ca3de"></div>
<div class="abs swatch" style="left:912px;background:#f7f7f7"></div>
<div class="abs swatch-code" style="left:813px">#0d193f</div>
<div class="abs swatch-code" style="left:860px">#0d193f</div>
<div class="abs swatch-code" style="left:906px">#f7f7f7</div>

<!-- Responsive hero screens -->
<div class="screen" style="left:351px;top:305px;width:587px;height:333px">
  <div class="s-top" style="height:12px;padding:0 80px;font-size:5px"><span>✉ contact@korvend.vc</span><span class="li-sq" style="width:8px;height:8px"></span></div>
  <div class="s-nav" style="height:45px;padding:0 80px"><span class="s-logo" style="font-size:13px">Korvend Capital</span>
    <span class="s-links" style="gap:20px;font-size:6px"><span class="on">Home</span><span>About</span><span>Team</span><span>Contact</span></span></div>
  <div class="s-hero" role="img" aria-label="Photo of colleagues collaborating over a digital table" style="top:57px">
    <div class="s-copy" style="left:80px;top:95px;width:400px">
      <div class="s-label" style="font-size:6.5px">We're a team of founders and seasoned professionals</div>
      <h2 style="font-size:20px;line-height:29px;margin-top:6px">Helping Ambitious Entrepreneurs<br>Start and Build Great Companies</h2>
      <p style="font-size:6px;line-height:13px;margin-top:10px">Korvend Capital is an early-stage fund with expertise in data, digital marketing, and technology.<br>In collaboration with Meridan University, we are dedicated to helping founders in the early</p>
    </div>
  </div>
</div>
<div class="screen" style="left:159px;top:551px;width:365px;height:225px">
  <div class="s-top" style="height:8px;padding:0 48px;font-size:3.5px"><span>✉ contact@korvend.vc</span><span class="li-sq" style="width:6px;height:6px"></span></div>
  <div class="s-nav" style="height:30px;padding:0 48px"><span class="s-logo" style="font-size:8px">Korvend Capital</span>
    <span class="s-links" style="gap:12px;font-size:4px"><span class="on">Home</span><span>About</span><span>Team</span><span>Contact</span></span></div>
  <div class="s-hero" role="img" aria-label="Photo of colleagues collaborating over a digital table" style="top:38px">
    <div class="s-copy" style="left:48px;top:57px;width:240px">
      <div class="s-label" style="font-size:4px">We're a team of founders and seasoned professionals</div>
      <h2 style="font-size:12.5px;line-height:18px;margin-top:4px">Helping Ambitious Entrepreneurs<br>Start and Build Great Companies</h2>
      <p style="font-size:4px;line-height:8px;margin-top:6px">Korvend Capital is an early-stage fund with expertise in data, digital marketing, and technology. In collaboration with Meridan University, we are dedicated to helping founders in the early stages of their journey.</p>
      <span class="s-btn" style="width:44px;height:14px;font-size:3.5px;margin-top:8px">CONTACT US</span>
    </div>
  </div>
</div>
<div class="screen" style="left:964px;top:553px;width:120px;height:247px">
  <div class="s-top" style="height:10px;padding:0 8px;font-size:3.5px"><span>✉ contact@korvend.vc</span><span class="li-sq" style="width:6px;height:6px"></span></div>
  <div class="s-nav" style="height:36px;padding:0 8px"><span class="s-logo" style="font-size:8px">Korvend</span><span style="color:var(--blue);font-size:8px">≡</span></div>
  <div class="s-hero" role="img" aria-label="Photo of colleagues collaborating over a digital table" style="top:46px">
    <div class="s-copy" style="left:8px;top:36px;width:104px">
      <h2 style="font-size:9.5px;line-height:15px">Helping Ambitious Entrepreneurs Start and Build Great Companies</h2>
      <p style="font-size:3.5px;line-height:7.5px;margin-top:4px">Korvend Capital is an early-stage fund with expertise in data, digital marketing, and technology. In collaboration with Meridan University, we are dedicated to helping founders in the early stages of their journey.</p>
      <span class="s-btn" style="width:50px;height:17px;font-size:4px;margin-top:8px">CONTACT US</span>
    </div>
  </div>
</div>

<!-- Desktop page -->
<div class="page d-page">
  <div class="topbar" style="height:22px;padding:0 97px;font-size:7px">
    <span>✉ contact@korvend.vc</span><span class="li-sq" style="width:12px;height:12px"></span>
  </div>
  <nav class="navbar" style="height:55px;padding:0 97px">
    <span class="logo-text" style="font-size:17px">Korvend Capital</span>
    <ul class="nav-links" style="gap:28px;font-size:8.5px;color:#555">
      <li class="active">Home</li><li>About</li><li>Team</li><li>Contact</li>
    </ul>
  </nav>
  <section class="hero" role="img" aria-label="Photo of colleagues collaborating over a digital planning table" style="height:458px">
    <div class="hero-copy" style="left:97px;top:122px;width:480px">
      <div class="eyebrow" style="font-size:8px">We're a team of founders and seasoned professionals</div>
      <h1 class="serif-title" style="font-size:28px;line-height:37px;margin-top:9px">Helping Ambitious Entrepreneurs<br>Start and Build Great Companies</h1>
      <p style="font-size:8.5px;line-height:17.5px;margin-top:18px">Korvend Capital is an early-stage fund with expertise in data, digital marketing, and technology.<br>In collaboration with Meridan University, we are dedicated to helping founders in the early<br>stages of their journey.</p>
      <a class="btn" style="width:86px;height:35px;font-size:8px;margin-top:21px">CONTACT US</a>
    </div>
  </section>
  <section class="about" style="height:339px">
    <div class="abs" style="left:97px;top:58px;width:270px">
      <div class="eyebrow" style="font-size:7px">Introduction</div>
      <h2 class="serif-title" style="font-size:26px;margin-top:6px">About Korvend Capital</h2>
      <p style="font-size:7.5px;line-height:16.5px;margin-top:22px">We are a team of founders and seasoned professionals who have taken the entrepreneurial journey ourselves in starting and building <a href="#">successful companies</a>. Now as investors, we are excited to help the future entrepreneurs succeed and win.</p>
      <p style="font-size:7.5px;line-height:16.5px;margin-top:7px">Our focus is helping pre-seed and seed startups launch and scale their companies. We believe in investing in ambitious entrepreneurs and using our expertise helping them launch &amp; scale successful products &amp;services.</p>
      <p style="font-size:7.5px;line-height:16.5px;margin-top:7px">We are delighted to work with tomorrow's innovators and help them achieve their entrepreneurial vision</p>
    </div>
    <div class="abs collage" role="img" aria-label="Collage of startup team photos" style="left:398px;top:71px;width:233px;height:213px"></div>
  </section>
  <section class="team" style="height:440px">
    <div class="abs" style="left:0;right:0;top:56px;text-align:center">
      <div class="eyebrow" style="font-size:7px;color:#555">Members</div>
      <h2 class="serif-title" style="font-size:26px;color:var(--navy);margin-top:6px">Our Team</h2>
    </div>
    <div class="member" style="left:97px;top:120px;width:169px;height:269px">
      <div class="portrait" role="img" aria-label="Portrait of Nadav Corvish" style="margin:12px 12px 0;height:172px"></div>
      <div class="name" style="font-size:11px;margin-top:13px">Nadav Corvish</div>
      <div class="role" style="font-size:7.5px;margin-top:6px">General partner</div>
      <span class="li-sq blue" style="width:11px;height:11px;margin-top:10px"></span>
    </div>
    <div class="member" style="left:280px;top:120px;width:169px;height:269px">
      <div class="portrait" role="img" aria-label="Portrait of Tomas Dune-Rok" style="margin:12px 12px 0;height:172px"></div>
      <div class="name" style="font-size:11px;margin-top:13px">Tomas Dune-Rok</div>
      <div class="role" style="font-size:7.5px;margin-top:6px">General partner</div>
      <span class="li-sq blue" style="width:11px;height:11px;margin-top:10px"></span>
    </div>
    <div class="member" style="left:463px;top:120px;width:169px;height:269px">
      <div class="portrait" role="img" aria-label="Portrait of Jon Mirtaveski" style="margin:12px 12px 0;height:172px"></div>
      <div class="name" style="font-size:11px;margin-top:13px">Jon Mirtaveski</div>
      <div class="role" style="font-size:7.5px;margin-top:6px">General partner</div>
      <span class="li-sq blue" style="width:11px;height:11px;margin-top:10px"></span>
    </div>
    <div class="abs" style="left:97px;width:536px;top:438px;height:1px;background:var(--line)"></div>
  </section>
  <section class="contact" style="height:229px">
    <div class="abs" style="left:97px;top:55px">
      <div class="eyebrow" style="font-size:7px">Contact</div>
      <h2 class="serif-title" style="font-size:25px;line-height:37px;color:var(--navy);margin-top:9px">For general inquiries,<br>you can email us at</h2>
      <a href="#" style="display:block;font-size:7.5px;color:#444;margin-top:12px;text-decoration:underline">contact@korvend.vc</a>
    </div>
    <div class="abs" style="left:526px;top:59px;width:107px">
      <div class="office-name" style="font-size:11px">New York</div>
      <div class="office-addr" style="font-size:7.5px;margin-top:9px;padding-bottom:9px;border-bottom:1px solid var(--line)">New York Address Goes Here</div>
      <div class="office-name" style="font-size:11px;margin-top:40px">Israel</div>
      <div class="office-addr" style="font-size:7.5px;margin-top:9px;padding-bottom:9px;border-bottom:1px solid var(--line)">Israel Address Goes Here</div>
    </div>
  </section>
  <footer class="footer" style="height:262px">
    <div class="abs" style="left:97px;top:56px;width:170px">
      <div class="logo-text" style="font-size:16px;color:#fff">Korvend Capital</div>
      <p style="font-size:6.5px;line-height:17px;margin-top:18px">Korvend Capital is an early-stage fund with expertise in data, digital marketing, and technology. In collaboration with Meridan University, we are dedicated to helping founders in the early stages of their journey</p>
    </div>
    <div class="abs" style="left:347px;top:54px">
      <div class="f-head" style="font-size:17px">Quick Links</div>
      <ul style="font-size:6.5px;line-height:17px;margin-top:18px"><li>Home</li><li>About</li><li>Team</li><li>Contact</li></ul>
    </div>
    <div class="abs" style="left:554px;top:54px">
      <div class="f-head" style="font-size:17px">Contact Us</div>
      <div style="font-size:6.5px;margin-top:24px">contact@korvend.vc</div>
      <span class="li-sq" style="width:12px;height:12px;margin-top:12px"></span>
    </div>
    <div class="abs" style="left:97px;width:536px;top:180px;height:1px;background:rgba(255,255,255,.15)"></div>
    <div class="abs" style="left:0;right:0;top:205px;text-align:center;font-size:6.5px">Copyright © 2021 - Korvend Capital - All Rights Reserved</div>
  </footer>
</div>

<!-- Mobile page -->
<div class="page" style="left:961px;top:859px;width:137px;height:1805px">
  <div class="topbar" style="height:12px;padding:0 9px;font-size:4.5px"><span>✉ contact@korvend.vc</span><span class="li-sq" style="width:7px;height:7px"></span></div>
  <nav class="navbar" style="height:39px;padding:0 9px"><span class="logo-text" style="font-size:10px">Korvend</span><span style="color:var(--blue);font-size:10px">≡</span></nav>
  <section class="hero" role="img" aria-label="Photo of colleagues collaborating over a digital planning table" style="height:252px">
    <div class="hero-copy" style="left:9px;top:46px;width:119px">
      <h1 class="serif-title" style="font-size:11.5px;line-height:18px">Helping Ambitious Entrepreneurs Start and Build Great Companies</h1>
      <p style="font-size:4px;line-height:11.5px;margin-top:5px">Korvend Capital is an early-stage fund with expertise in data, digital marketing, and technology. In collaboration with Meridan University, we are dedicated to helping founders in the early stages of their journey.</p>
      <a class="btn" style="width:56px;height:20px;font-size:4.5px;margin-top:10px">CONTACT US</a>
    </div>
  </section>
  <section class="about" style="height:335px">
    <div class="abs collage" role="img" aria-label="Collage of startup team photos" style="left:10px;top:27px;width:118px;height:114px"></div>
    <div class="abs" style="left:9px;top:157px;width:120px">
      <div class="eyebrow" style="font-size:4px">Introduction</div>
      <h2 class="serif-title" style="font-size:11px;margin-top:4px">About Korvend Capital</h2>
      <p style="font-size:3.6px;line-height:11px;margin-top:8px">We are a team of founders and seasoned professionals who have taken the entrepreneurial journey ourselves in starting and building <a href="#">successful companies</a>. Now as investors, we are excited to help the future entrepreneurs succeed and win.</p>
      <p style="font-size:3.6px;line-height:11px;margin-top:3px">Our focus is helping pre-seed and seed startups launch and scale their companies. We believe in investing in ambitious entrepreneurs and using our expertise helping them launch &amp; scale successful products &amp;services.</p>
      <p style="font-size:3.6px;line-height:11px;margin-top:3px">We are delighted to work with tomorrow's innovators and help them achieve their entrepreneurial vision</p>
    </div>
  </section>
  <section class="team" style="height:622px">
    <div class="abs" style="left:9px;top:30px">
      <div class="eyebrow" style="font-size:4px;color:#555">Members</div>
      <h2 class="serif-title" style="font-size:11px;color:var(--navy);margin-top:4px">Our Team</h2>
    </div>
    <div class="member" style="left:9px;top:68px;width:119px;height:175px">
      <div class="portrait" role="img" aria-label="Portrait of Nadav Corvish" style="margin:8px 9px 0;height:112px"></div>
      <div class="name" style="font-size:6.5px;margin-top:10px">Nadav Corvish</div>
      <div class="role" style="font-size:4px;margin-top:4px">General partner</div>
      <span class="li-sq blue" style="width:8px;height:8px;margin-top:5px"></span>
    </div>
    <div class="member" style="left:9px;top:254px;width:119px;height:173px">
      <div class="portrait" role="img" aria-label="Portrait of Tomas Dune-Rok" style="margin:8px 9px 0;height:112px"></div>
      <div class="name" style="font-size:6.5px;margin-top:10px">Tomas Dune-Rok</div>
      <div class="role" style="font-size:4px;margin-top:4px">General partner</div>
      <span class="li-sq blue" style="width:8px;height:8px;margin-top:5px"></span>
    </div>
    <div class="member" style="left:9px;top:438px;width:119px;height:178px">
      <div class="portrait" role="img" aria-label="Portrait of Jon Mirtaveski" style="margin:8px 9px 0;height:112px"></div>
      <div class="name" style="font-size:6.5px;margin-top:10px">Jon Mirtaveski</div>
      <div class="role" style="font-size:4px;margin-top:4px">General partner</div>
      <span class="li-sq blue" style="width:8px;height:8px;margin-top:5px"></span>
    </div>
  </section>
  <section class="contact" style="height:227px">
    <div class="abs" style="left:9px;top:54px;width:124px">
      <div class="eyebrow" style="font-size:4px">Contact</div>
      <h2 class="serif-title" style="font-size:11px;line-height:18px;color:var(--navy);margin-top:5px">For general inquiries, you can email us at</h2>
      <a href="#" style="display:block;font-size:4px;color:#444;margin-top:7px;text-decoration:underline">contact@korvend.vc</a>
      <div class="office-name" style="font-size:6.5px;margin-top:20px">New York</div>
      <div class="office-addr" style="font-size:3.8px;margin-top:6px">New York Address Goes Here</div>
      <div class="office-name" style="font-size:6.5px;margin-top:22px">Israel</div>
      <div class="office-addr" style="font-size:3.8px;margin-top:6px">Israel Address Goes Here</div>
    </div>
  </section>
  <footer class="footer" style="height:318px">
    <div class="abs" style="left:9px;top:34px;width:120px">
      <div class="logo-text" style="font-size:10px;color:#fff">Korvend</div>
      <p style="font-size:3.6px;line-height:11px;margin-top:8px">Korvend Capital is an early-stage fund with expertise in data, digital marketing, and technology. In collaboration with Meridan University, we are dedicated to helping founders in the early stages of their journey</p>
      <div class="f-head" style="font-size:9px;margin-top:12px">Quick Links</div>
      <ul style="font-size:3.6px;line-height:11px;margin-top:10px"><li>Home</li><li>About</li><li>Team</li><li>Contact</li></ul>
      <div class="f-head" style="font-size:9px;margin-top:14px">Contact Us</div>
      <div style="font-size:3.6px;margin-top:14px">contact@korvend.vc</div>
      <span class="li-sq" style="width:8px;height:8px;margin-top:5px"></span>
    </div>
    <div class="abs" style="left:0;right:0;top:284px;text-align:center;font-size:3.6px">Copyright © 2021 - Korvend Capital - All Rights Reserved</div>
  </footer>
</div>

<!-- Section labels -->
<div class="abs side-label" style="left:112px;top:2296px">LAPTOP / DESKTOP</div>
<div class="abs side-label" style="left:920px;top:2178px">MOBILE</div>

</body>
</html>
```